CD-Cover Desig für neues Album eines Liedermacher-Duos
Zielgruppe
Wir sind ein Liedermacher-Duo und benötigen für unser neues Album mit dem Titel 'Kiesel' ein Cover.
Infos über den Themenbereich der Songs findet man hier: https://www.vorhabenwerk.de/cd-kiesel
Aufgabenstellung
Cover könnte schlicht sein... oder auch kreativ verspielt mit warmen Farben und Formen... aber nicht kitschig.
'Kiesel' im Sinne von Geborgenheit also kein verzehrendes Feuer.. eher sonnig.
Evtl. könnte man unsere beiden Hauptinstrumente (Geige und Gitarre) andeuten.
Sonst stehen auf dem Cover nur noch unsere Namen: Dorothea Lindner & Jörg Haberl

```html
<!DOCTYPE html>
<html lang="de">
<head>
<meta charset="utf-8">
<title>Kiesel – Dorothea Lindner &amp; Jörg Haberl</title>
<link rel="stylesheet" href="https://fonts.googleapis.com/css2?family=Barlow:wght@400&family=Yellowtail&display=block">
<style>
  :root {
    --page: #ffffff;
    --sky-top: #d8703a;
    --sky-mid: #ee9550;
    --sky-warm: #f2a24e;
    --sky-low: #c0703f;
    --ground: #6a4032;
    --frame: #ffd58a;
    --label: #ffffff;
    --title: rgba(255, 232, 196, 0.55);
  }
  html, body {
    margin: 0;
    padding: 0;
    width: 1200px;
    height: 1200px;
    overflow: hidden;
    background: var(--page);
  }
  .cover {
    position: absolute;
    left: 60px;
    top: 60px;
    width: 1080px;
    height: 1080px;
    overflow: hidden;
  }
  .cover__photo {
    position: absolute;
    inset: 0;
    background:
      radial-gradient(ellipse at 70% 55%, rgba(248, 178, 80, 0.55) 0, rgba(248, 178, 80, 0) 55%),
      linear-gradient(180deg, var(--sky-top) 0%, var(--sky-mid) 38%, var(--sky-warm) 55%, var(--sky-low) 82%, var(--ground) 100%);
  }
  .cover__frame {
    position: absolute;
    left: 22px;
    top: 22px;
    width: 1030px;
    height: 1030px;
    border: 3.5px solid var(--frame);
  }
  .cover__artists {
    position: absolute;
    left: 62px;
    top: 62px;
    width: 344px;
    height: 106px;
    border: 2px solid var(--label);
    box-sizing: border-box;
    display: flex;
    flex-direction: column;
    justify-content: center;
    align-items: center;
    font-family: "Barlow", sans-serif;
    font-weight: 400;
    font-size: 34px;
    line-height: 42px;
    color: var(--label);
    text-align: center;
  }
  .cover__title {
    position: absolute;
    left: 4px;
    top: 600px;
    margin: 0;
    font-family: "Yellowtail", cursive;
    font-weight: 400;
    font-size: 360px;
    line-height: 1;
    color: var(--title);
    white-space: nowrap;
  }
</style>
</head>
<body>
  <main class="cover">
    <div class="cover__photo" role="img" aria-label="Fotografie: Gräser und Ähren im Gegenlicht vor tief stehender Abendsonne in warmem Orange"></div>
    <div class="cover__frame"></div>
    <div class="cover__artists">
      <span>Dorothea Lindner &amp;</span>
      <span>Jörg Haberl</span>
    </div>
    <h1 class="cover__title">Kiesel</h1>
  </main>
</body>
</html>
```